Vorn Solutions: searching for a flyer to trow in letterboxes for properties we are interested in

Hello ,

Introduction:
We are a company based in Luxembourg called "Vorn Solutions". We are specialized in buying properties on which we develop and build constructions before selling them.

Informations for the flyer:
We need a flyer to trow into the letter boxes of property owners letting them know that we are interested in buying their property, if they are interested they can give us a call.

The text for the flyer/letter is in the attachment called >>2020-03-11_VS_Text for flyer,letter there might be slight changes<<.

We need to look competent, professional and financially stable.

The flyer needs to be short and not over welling with information otherwise it will land in the trash.

We have decided that we don't want real pictures on the flyer, but shapes of any kind, blue prints, drawings are fine.

Format should be in DIN A4. We plan to print the flyer on both sides in two different languages, in other words the design will be the same on both sides only the text will be in a different language.

I also added our current logo and here is the design of the website that is under construction at the moment http://www.vornsolutions.example/. The logo's color can be changed into a different blue or uni color (all white or all black).
Updates

Hi, First time user the howl thing started faster as expected. Furthermore, I need to catch my boss to discust the project with him and he is on a lot of meetings. Please give us a little bit more time. Thanks

Target Market(s)

Property owners

Requirements
Must have
• email, phone number, tax number (RCS), Tax number , matriculation and address.
see word file in attachment for information
Nice to have
• Our company logo, in one form or an other, you can be creative, the logo is in the attachment.
Should not have
• Real pictures

```html
<!DOCTYPE html>
<html lang="fr">
<head>
<meta charset="utf-8">
<title>Vorn Solutions – Flyer</title>
<link href="https://fonts.googleapis.com/css2?family=Bebas+Neue&family=Montserrat:wght@400;600&family=Open+Sans:wght@400&display=swap" rel="stylesheet">
<style>
  :root {
    --brand-blue: #0f5480;
    --brand-orange: #e8470f;
    --ink: #555a5e;
    --rule: #2e2e2e;
    --paper: #ffffff;
    --stage: #ffffff;
  }
  * { margin: 0; padding: 0; box-sizing: border-box; }
  html, body { width: 1200px; height: 821px; overflow: hidden; background: var(--stage); }
  .canvas { position: relative; width: 1200px; height: 821px; }

  .page {
    position: absolute; top: 0; width: 581px; height: 821px;
    background: var(--paper); overflow: hidden;
    box-shadow: 0 0 6px rgba(0,0,0,.18);
  }
  .page--front { left: 0; }
  .page--back { left: 619px; }

  .brand-panel {
    position: absolute; left: 0; top: 0; width: 236px; height: 337px;
    background: var(--brand-blue);
    display: flex; align-items: center; justify-content: center;
  }
  .brand-panel__name {
    font-family: "Bebas Neue", sans-serif; color: #fff;
    font-size: 34px; letter-spacing: .5px; margin-top: 20px;
  }
  .hero-visual {
    position: absolute; left: 236px; top: 0; width: 345px; height: 305px;
    background:
      radial-gradient(circle at 45% 0%, #fffdf4 0%, rgba(255,250,230,.9) 14%, rgba(255,255,255,0) 40%),
      linear-gradient(100deg, #c7942f 0%, #3d5f86 28%, #1e3d66 45%, #c9a24a 58%, #2a4a78 72%, #e9eef6 88%, #5a78b0 100%);
  }
  .hero-band {
    position: absolute; left: 236px; top: 305px; width: 345px; height: 8px;
    background: var(--brand-orange);
  }
  .hero-fold { position: absolute; left: 236px; top: 313px; }

  .headline {
    position: absolute; left: 0; right: 0; top: 385px; text-align: center;
    font-family: "Bebas Neue", sans-serif; font-size: 52px; line-height: 1;
    color: var(--brand-orange); letter-spacing: .3px;
  }
  .headline__suffix { color: var(--brand-blue); }
  .headline-rule {
    position: absolute; top: 454px; left: 184px; width: 213px; height: 3px;
    background: var(--rule);
  }
  .version-label {
    position: absolute; left: 0; right: 0; top: 482px; text-align: center;
    font-family: "Open Sans", sans-serif; font-size: 17px; color: var(--brand-blue);
  }
  .version-label em { font-style: normal; color: var(--brand-orange); }
  .letter {
    position: absolute; left: 78px; width: 425px; top: 512px; text-align: center;
    font-family: "Montserrat", sans-serif; font-size: 9.6px; line-height: 11.8px;
    color: var(--ink);
  }

  .footer-band {
    position: absolute; left: 0; top: 675px; width: 581px; height: 8px;
    background: var(--brand-orange);
  }
  .footer {
    position: absolute; left: 0; top: 683px; width: 581px; height: 138px;
    background: var(--brand-blue); color: #fff;
    font-family: "Montserrat", sans-serif;
  }
  .portrait { position: absolute; left: 243px; top: 627px; }

  .contact-phone {
    position: absolute; left: 0; right: 0; top: 62px;
    display: flex; align-items: center; justify-content: center; gap: 16px;
    font-weight: 600; font-size: 23px;
  }
  .contact-line {
    position: absolute; left: 0; right: 0; top: 100px;
    display: flex; align-items: center; justify-content: center;
    font-size: 13px; white-space: nowrap;
  }
  .contact-line__item { display: flex; align-items: center; gap: 12px; }
  .contact-line__divider { margin: 0 22px; }
</style>
</head>
<body>
<div class="canvas">

  <section class="page page--front">
    <div class="brand-panel"><span class="brand-panel__name">Vorn Solutions</span></div>
    <div class="hero-visual" role="img" aria-label="Photo of glass skyscrapers seen from below against a sunlit sky"></div>
    <div class="hero-band"></div>
    <svg class="hero-fold" width="22" height="24" viewBox="0 0 22 24"><polygon points="0,0 22,0 0,24" fill="#0b3d5e"/></svg>

    <h1 class="headline">Vorn Solutions <span class="headline__suffix">Sàrl</span></h1>
    <div class="headline-rule"></div>
    <p class="version-label">FR VERSION FOR <em>ONE SIDE:</em></p>
    <p class="letter">
      Madame, Monsieur,<br>
      Ce courrier vous a été adressé, car votre propriété a attiré notre attention. Nous souhai-<br>terions discuter avec vous de son éventuel rachat par notre société.<br>
      En cas d’accord, nous vous assurons une décision rapide, un paiement garanti, et zéro frais d’intermédiare.<br>
      En attendant de vos nouvelles, nous restons à votre entière disposition pour tout renseignement.<br>
      Salutations distinguées,
    </p>

    <div class="footer-band"></div>
    <footer class="footer">
      <div class="contact-phone">
        <svg width="20" height="22" viewBox="0 0 24 24"><path fill="#e8470f" d="M6.6 10.8a15.1 15.1 0 0 0 6.6 6.6l2.2-2.2c.3-.3.7-.4 1-.2 1.1.4 2.3.6 3.6.6.6 0 1 .4 1 1V20c0 .6-.4 1-1 1A17 17 0 0 1 3 4c0-.6.4-1 1-1h3.5c.6 0 1 .4 1 1 0 1.3.2 2.5.6 3.6.1.3 0 .7-.2 1z"/></svg>
        <span>691 555 014</span>
      </div>
      <div class="contact-line">
        <span class="contact-line__item">
          <svg width="18" height="13" viewBox="0 0 18 13"><rect width="18" height="13" rx="1" fill="#e8470f"/><path d="M1 1l8 6 8-6" stroke="#0f5480" stroke-width="1.5" fill="none"/></svg>
          info@vornsolutions.example
        </span>
        <span class="contact-line__divider">|</span>
        <span class="contact-line__item">
          <svg width="11" height="15" viewBox="0 0 12 16"><path fill="#e8470f" d="M6 0a6 6 0 0 0-6 6c0 4.5 6 10 6 10s6-5.5 6-10a6 6 0 0 0-6-6zm0 8.5A2.5 2.5 0 1 1 6 3.5a2.5 2.5 0 0 1 0 5z"/></svg>
          17 rue des Forges,&nbsp; L-3290 Kessange
        </span>
      </div>
    </footer>
    <svg class="portrait" width="96" height="96" viewBox="0 0 96 96" role="img" aria-label="Portrait photo of a smiling construction worker in a hard hat">
      <defs><linearGradient id="portraitFillA" x1="0" y1="0" x2="1" y2="1"><stop offset="0" stop-color="#d9c9a8"/><stop offset=".5" stop-color="#8a6e52"/><stop offset="1" stop-color="#4d3b2c"/></linearGradient></defs>
      <polygon points="48,3 93,48 48,93 3,48" fill="url(#portraitFillA)" stroke="#e8470f" stroke-width="6"/>
    </svg>
  </section>

  <section class="page page--back">
    <div class="brand-panel"><span class="brand-panel__name">Vorn Solutions</span></div>
    <div class="hero-visual" role="img" aria-label="Photo of glass skyscrapers seen from below against a sunlit sky"></div>
    <div class="hero-band"></div>
    <svg class="hero-fold" width="22" height="24" viewBox="0 0 22 24"><polygon points="0,0 22,0 0,24" fill="#0b3d5e"/></svg>

    <h1 class="headline">Vorn Solutions <span class="headline__suffix">Sàrl</span></h1>
    <div class="headline-rule"></div>
    <p class="version-label">LU VERSION FOR THE <em>OTHER SIDE:</em></p>
    <p class="letter">
      Madame, Monsieur,<br>
      Dir kritt dëst Schreiwes well Är Proprietéit eis Opmierksamkeet zeréckbehalen huet.<br>
      Mir géinge gär mat Iech iwwert d’Méiglechkeet, datt eise Betrib se opkeeft, diskutéieren. Mir versécheren Iech e séieren Entscheedungsprozess, garantéieren d’Bezuelung a verrechne keng Drëttkäschten.<br>
      Mir géingen eis freeën, vun Iech ze héieren, a sti ganz zu Ärer Verfügung fir zousätzlech Informatiounen. Mat beschte Gréiss, D’Equipe vun Vorn Solutions
    </p>

    <div class="footer-band"></div>
    <footer class="footer">
      <div class="contact-phone">
        <svg width="20" height="22" viewBox="0 0 24 24"><path fill="#e8470f" d="M6.6 10.8a15.1 15.1 0 0 0 6.6 6.6l2.2-2.2c.3-.3.7-.4 1-.2 1.1.4 2.3.6 3.6.6.6 0 1 .4 1 1V20c0 .6-.4 1-1 1A17 17 0 0 1 3 4c0-.6.4-1 1-1h3.5c.6 0 1 .4 1 1 0 1.3.2 2.5.6 3.6.1.3 0 .7-.2 1z"/></svg>
        <span>691 555 014</span>
      </div>
      <div class="contact-line">
        <span class="contact-line__item">
          <svg width="18" height="13" viewBox="0 0 18 13"><rect width="18" height="13" rx="1" fill="#e8470f"/><path d="M1 1l8 6 8-6" stroke="#0f5480" stroke-width="1.5" fill="none"/></svg>
          info@vornsolutions.example
        </span>
        <span class="contact-line__divider">|</span>
        <span class="contact-line__item">
          <svg width="11" height="15" viewBox="0 0 12 16"><path fill="#e8470f" d="M6 0a6 6 0 0 0-6 6c0 4.5 6 10 6 10s6-5.5 6-10a6 6 0 0 0-6-6zm0 8.5A2.5 2.5 0 1 1 6 3.5a2.5 2.5 0 0 1 0 5z"/></svg>
          17 rue des Forges,&nbsp; L-3290 Kessange
        </span>
      </div>
    </footer>
    <svg class="portrait" width="96" height="96" viewBox="0 0 96 96" role="img" aria-label="Portrait photo of a smiling construction worker in a hard hat">
      <defs><linearGradient id="portraitFillB" x1="0" y1="0" x2="1" y2="1"><stop offset="0" stop-color="#d9c9a8"/><stop offset=".5" stop-color="#8a6e52"/><stop offset="1" stop-color="#4d3b2c"/></linearGradient></defs>
      <polygon points="48,3 93,48 48,93 3,48" fill="url(#portraitFillB)" stroke="#e8470f" stroke-width="6"/>
    </svg>
  </section>

</div>
</body>
</html>
```